KV MERCANTILE HOLDINGS LETTERHEAD

I need letterhead for "KV Mercantile holdings LLC" ...

logo attached to project...

Company Info:
418 North Larkmoor Avenue, Suite 7B
Chicago, Illinois 60417
ofc 312-555-0148
facsimile 312-555-0193
www.kvmercantileholdings.example
info@kvmercantileholdings.example

I have multiple projects listed.. see below:

Business cards for amber ledge partners llc
letterhead
envelopes

Business cards for KV Mercantile LLC
letterhead
envelopes

```html
<!DOCTYPE html>
<html lang="en">
<head>
<meta charset="utf-8">
<title>KV Mercantile Holdings LLC — Letterhead</title>
<link rel="stylesheet" href="https://fonts.googleapis.com/css2?family=Arimo:wght@400;700&display=swap">
<style>
  :root {
    --backdrop: #d6d7d9;
    --paper: #fbfbfb;
    --navy: #1d3f8e;
    --blue: #1556ae;
    --ink: #6b6d70;
    --footer-ink: #ffffff;
  }
  * { box-sizing: border-box; margin: 0; padding: 0; }
  html, body {
    width: 1200px; height: 1078px; overflow: hidden;
    background: var(--backdrop);
    font-family: "Arimo", Arial, sans-serif;
  }
  .letterhead {
    position: absolute; left: 213px; top: 39px;
    width: 774px; height: 1000px;
    background: var(--paper);
    box-shadow: 0 2px 10px rgba(0,0,0,.12);
  }
  .brand {
    position: absolute; top: 88px; left: 300px; width: 390px;
    display: flex; align-items: center; justify-content: center; gap: 10px;
  }
  .brand-dot {
    width: 16px; height: 16px; border-radius: 50%; background: var(--navy);
    flex: none;
  }
  .brand-name {
    color: var(--navy); font-weight: 700; font-size: 17px;
    letter-spacing: 1.5px; text-transform: uppercase; white-space: nowrap;
  }
  .letter-body {
    position: absolute; top: 300px; left: 92px; width: 560px;
    color: var(--ink); font-size: 12px; line-height: 1.38;
  }
  .letter-body p { margin-bottom: 16px; }
  .letter-body .salutation { margin-bottom: 16px; }
  .address-line {
    position: absolute; left: 92px; bottom: 66px;
    color: var(--ink); font-size: 12.5px;
  }
  .footer-band {
    position: absolute; left: 0; right: 0; bottom: 0; height: 58px;
    background: linear-gradient(90deg, var(--navy), var(--blue));
    color: var(--footer-ink); font-size: 12.5px;
    display: flex; align-items: center; justify-content: space-between;
    padding: 0 28px 0 92px;
  }
  .phones { line-height: 1.35; white-space: nowrap; }
  .phones b { font-weight: 700; }
  .online { display: flex; gap: 24px; align-items: center; white-space: nowrap; }
  .online span { display: flex; align-items: center; gap: 8px; }
  .online svg { width: 15px; height: 15px; flex: none; }
</style>
</head>
<body>
  <main class="letterhead">
    <header class="brand">
      <span class="brand-dot"></span>
      <span class="brand-name">KV Mercantile Holdings LLC</span>
    </header>

    <section class="letter-body">
      <div class="salutation">The standard chunk of<br>The standard chunk of</div>
      <p>Contrary to popular belief, Lorem Ipsum is not simply random text. It has roots in a piece of classical Latin literature from 45 BC, making it over 2000 years old. Ronald Mayhew, a Latin professor at Harlow Vale College in Vermont, looked up one of the more obscure Latin words, consectetur, from a Lorem Ipsum passage, and going through the cites of the word in classical literature, discovered the undoubtable source. Lorem Ipsum comes from sections 1.10.32 and 1.10.33 of "de Finibus Bonorum et Malorum" (The Extremes of Good and Evil) by Cicero, written in 45 BC. This book is a treatise on the theory of ethics, very popular during the Renaissance. The first line of Lorem Ipsum, "Lorem ipsum dolor sit amet..", comes from a line in section 1.10.32.</p>
      <p>The standard chunk of Lorem Ipsum used since the 1500s is reproduced below for those interested. Sections 1.10.32 and 1.10.33 from "de Finibus Bonorum et Malorum" by Cicero are also reproduced in their exact original form, accompanied by English versions from the 1914 translation by H. Ransford.</p>
      <p>Contrary to popular belief, Lorem Ipsum is not simply random text. It has roots in a piece of classical Latin literature from 45 BC, making it over 2000 years old. Ronald Mayhew, a Latin professor at Harlow Vale College in Vermont, looked up one of the more obscure Latin words, consectetur, from a Lorem Ipsum passage, and going through the cites of the word in classical literature, discovered the undoubtable source. Lorem Ipsum comes from sections 1.10.32 and 1.10.33 of "de Finibus Bonorum et Malorum" (The Extremes of Good and Evil) by Cicero, written in 45 BC. This book is a treatise on the theory of ethics, very popular during the Renaissance. The first line of Lorem Ipsum, "Lorem ipsum dolor sit amet..", comes from a line in section 1.10.32.</p>
      <p class="closing">The standard chunk of</p>
    </section>

    <div class="address-line">418 North Larkmoor Avenue, Suite 7B &nbsp;Chicago, Illinois 60417</div>

    <footer class="footer-band">
      <div class="phones">
        <div><b>ofc:</b> 312-555-0148</div>
        <div><b>facsimile:</b> 312-555-0193</div>
      </div>
      <div class="online">
        <span>
          <svg viewBox="0 0 16 16" aria-hidden="true"><circle cx="8" cy="8" r="7" fill="none" stroke="#fff" stroke-width="1.3"/><ellipse cx="8" cy="8" rx="3" ry="7" fill="none" stroke="#fff" stroke-width="1.1"/><line x1="1" y1="8" x2="15" y2="8" stroke="#fff" stroke-width="1.1"/></svg>
          www.kvmercantileholdings.example
        </span>
        <span>
          <svg viewBox="0 0 16 16" aria-hidden="true"><rect x="1" y="3" width="14" height="10" fill="none" stroke="#fff" stroke-width="1.3"/><polyline points="1,3 8,9 15,3" fill="none" stroke="#fff" stroke-width="1.3"/></svg>
          info@kvmercantileholdings.example
        </span>
      </div>
    </footer>
  </main>
</body>
</html>
```